New shirt company looking for a fun and edgy online retail website design

We're a new company looking for a simple yet attractive website to sell shirts/tops to a mostly younger female audience. Our name is Tilvo Shirt Co. and the ArtPavilion logo is uploaded. We're thinking a home page, three separate pages for our shirt "collections", and a contact page/cart page for a grand total of 5 pages. We'd like the website to be coded, easy for the consumer to navigate/shop/checkout, and easy to link to various social media platforms and online websites. For colors, we're aiming for various blues, light grey, and maybe tan/khaki. Our goal is to launch with approximately 20-30 tops/shirts (or 7-10) per page. Please let us know if you have any questions and thank you for helping us! We are very excited to see what is created!

Target Market(s)

Female teens to early twenties

Coding

Coded - Design and coding required

Number of Pages Required

3 page

Font styles to use
Decorative
Script

Colors
cee9f5
85cae6
33a6d7
0393ce
cfdfed
85acd3

Requirements
Must have
• Online shopping/purchasing capabilities, dropdowns to select sizes for each item, easy to add/remove new or seasoned items.

```html
<!DOCTYPE html>
<html lang="en">
<head>
<meta charset="utf-8">
<title>Tilvo Shirt Co. — Collections</title>
<link rel="stylesheet" href="https://fonts.googleapis.com/css2?family=Poppins:wght@500;600&family=Great+Vibes&display=swap">
<style>
:root{
  --blue-a:#2b86b9;
  --blue-b:#0b5ea6;
  --amber:#ffad00;
  --violet-a:#6a2ddf;
  --violet-b:#7842e0;
  --mist:#eef0ef;
  --logo-bg:#8fd0ee;
  --logo-ink:#1f5fa0;
  --button:#ffb000;
  --ink-dark:#111111;
  --ink-light:#ffffff;
  --photo-blue:linear-gradient(180deg,#d9a77e 0%,#c98f8f 40%,#3f4b3a 80%,#9fb4cf 100%);
  --photo-amber:linear-gradient(180deg,#7a3f1f 0%,#f2c5b7 45%,#f6b9ad 75%,#4a2c20 100%);
  --photo-violet:linear-gradient(180deg,#2a2222 0%,#d8b79a 25%,#1a1a1a 45%,#111 100%);
  --photo-mist:linear-gradient(180deg,#a5744b 0%,#e6b9a0 35%,#8fb0d6 70%,#d9e3ef 100%);
}
*{margin:0;padding:0;box-sizing:border-box}
html,body{width:1200px;height:2699px;overflow:hidden}
body{font-family:"Poppins",sans-serif}
.collection{position:relative;width:1200px;height:674.75px;overflow:hidden}
.collection--top{background:linear-gradient(90deg,var(--blue-a),var(--blue-b));color:var(--ink-light)}
.collection--dress{background:var(--amber);color:var(--ink-dark)}
.collection--hoodie{background:linear-gradient(90deg,var(--violet-a),var(--violet-b));color:var(--ink-light)}
.collection--shirt{background:var(--mist);color:var(--ink-dark)}
.hero-photo{position:absolute;left:350px;top:14px;width:405px;height:661px;border-radius:180px 180px 0 0}
.nav{position:absolute;top:34px;list-style:none;font-weight:600;font-size:16px;line-height:24px}
.nav--left{left:44px}
.nav--right{right:44px;text-align:right}
.logo{position:absolute;left:529px;top:33px;width:142px;height:67px;background:var(--logo-bg);display:flex;align-items:center;justify-content:center;color:var(--logo-ink);font-weight:600;font-size:15px}
.thumb{position:absolute;top:249px;width:214px;height:175px}
.thumb--left{left:0}
.thumb--right{right:0}
.thumb--blue{background:linear-gradient(90deg,#c8a08a 0%,#b48f90 40%,var(--blue-a) 60%,var(--blue-b))}
.thumb--amber{background:linear-gradient(90deg,var(--amber) 45%,#e8b9a8 60%,#6b3b20 75%,var(--amber) 90%)}
.thumb--violet{background:linear-gradient(90deg,var(--violet-a) 42%,#1d1a1d 60%,#2a2424 80%,var(--violet-b))}
.thumb--mist{background:linear-gradient(90deg,var(--mist) 45%,#d7a98a 60%,#9fb9da 80%,var(--mist))}
.thumb--amber.thumb--left{background:linear-gradient(90deg,#e8b9a8 0%,#6b3b20 30%,#e8b9a8 50%,var(--amber) 70%)}
.thumb--violet.thumb--left{background:linear-gradient(90deg,#1d1a1d 0%,#2a2424 45%,var(--violet-a) 55%)}
.title{position:absolute;left:0;width:1200px;top:330px;text-align:center;font-family:"Great Vibes",cursive;font-size:240px;line-height:1;font-weight:400}
.title--light{color:var(--ink-light)}
.title--dark{color:var(--ink-dark)}
.more-info{position:absolute;left:535px;top:606px;width:129px;height:36px;background:var(--button);color:var(--ink-dark);font-weight:600;font-size:15px;display:flex;align-items:center;justify-content:center}
.social{position:absolute;left:44px;top:608px;display:flex;gap:14px;list-style:none}
.social li{width:35px;height:35px;border:2.5px solid currentColor;border-radius:50%}
</style>
</head>
<body>

<section class="collection collection--top">
  <div class="hero-photo" style="background:var(--photo-blue)" role="img" aria-label="Model in a pink knit sweater, cap and bomber jacket"></div>
  <ul class="nav nav--left"><li>Home</li><li>Collections</li><li>About Us</li></ul>
  <div class="logo">Tilvo Shirt Co.</div>
  <ul class="nav nav--right"><li>Cart (0)</li><li>Contact Us</li></ul>
  <div class="thumb thumb--left thumb--mist" role="img" aria-label="Preview of the shirt collection"></div>
  <div class="thumb thumb--right thumb--amber" role="img" aria-label="Preview of the dress collection"></div>
  <h2 class="title title--light">Top</h2>
  <a class="more-info">More Info</a>
  <ul class="social"><li aria-label="Social link"></li><li aria-label="Social link"></li><li aria-label="Social link"></li></ul>
</section>

<section class="collection collection--dress">
  <div class="hero-photo" style="background:var(--photo-amber)" role="img" aria-label="Model in sunglasses and a pink embroidered sweater"></div>
  <ul class="nav nav--left"><li>Home</li><li>Collections</li><li>About Us</li></ul>
  <div class="logo">Tilvo Shirt Co.</div>
  <ul class="nav nav--right"><li>Cart (0)</li><li>Contact Us</li></ul>
  <div class="thumb thumb--left thumb--blue" role="img" aria-label="Preview of the top collection"></div>
  <div class="thumb thumb--right thumb--violet" role="img" aria-label="Preview of the hoodie collection"></div>
  <h2 class="title title--dark">Dress</h2>
  <a class="more-info">More Info</a>
  <ul class="social"><li aria-label="Social link"></li><li aria-label="Social link"></li><li aria-label="Social link"></li></ul>
</section>

<section class="collection collection--hoodie">
  <div class="hero-photo" style="background:var(--photo-violet)" role="img" aria-label="Model in a black printed hoodie"></div>
  <ul class="nav nav--left"><li>Home</li><li>Collections</li><li>About Us</li></ul>
  <div class="logo">Tilvo Shirt Co.</div>
  <ul class="nav nav--right"><li>Cart (0)</li><li>Contact Us</li></ul>
  <div class="thumb thumb--left thumb--amber" role="img" aria-label="Preview of the dress collection"></div>
  <div class="thumb thumb--right thumb--mist" role="img" aria-label="Preview of the shirt collection"></div>
  <h2 class="title title--light">Hoodie</h2>
  <a class="more-info">More Info</a>
  <ul class="social"><li aria-label="Social link"></li><li aria-label="Social link"></li><li aria-label="Social link"></li></ul>
</section>

<section class="collection collection--shirt">
  <div class="hero-photo" style="background:var(--photo-mist)" role="img" aria-label="Model in a blue and white striped shirt"></div>
  <ul class="nav nav--left"><li>Home</li><li>Collections</li><li>About Us</li></ul>
  <div class="logo">Tilvo Shirt Co.</div>
  <ul class="nav nav--right"><li>Cart (0)</li><li>Contact Us</li></ul>
  <div class="thumb thumb--left thumb--violet" role="img" aria-label="Preview of the hoodie collection"></div>
  <div class="thumb thumb--right thumb--blue" role="img" aria-label="Preview of the top collection"></div>
  <h2 class="title title--dark">Shirt</h2>
  <a class="more-info">More Info</a>
  <ul class="social"><li aria-label="Social link"></li><li aria-label="Social link"></li><li aria-label="Social link"></li></ul>
</section>

</body>
</html>
```